Velbrook Health is a Direct primary office that needs a great flyer design

Velbrook Health has been rebranded with a new logo and website and need new flyers to fit in with our new model and direction. Please refer to velbrook.example for content. Attached is a possible layout.

```html
<!DOCTYPE html>
<html lang="en">
<head>
<meta charset="utf-8">
<title>Velbrook Health – Direct Primary Care Trifold</title>
<link href="https://fonts.googleapis.com/css2?family=Roboto:wght@400;500;700;900&display=swap" rel="stylesheet">
<style>
  :root{
    --navy:#0d1656;
    --navy-deep:#0a1248;
    --blue:#1b2a8f;
    --green:#0a8a3c;
    --green-bright:#1fb04a;
    --olive:#3b5a1a;
    --ink:#2b2b2b;
    --sky:#e2f2fb;
    --page:#e9ebee;
    --white:#ffffff;
  }
  *{box-sizing:border-box;margin:0;padding:0}
  html,body{width:1200px;height:903px;overflow:hidden;background:var(--page);font-family:"Roboto",Arial,sans-serif}
  .trifold{position:absolute;left:40px;top:20px;width:1120px;height:863px;display:flex;box-shadow:0 4px 16px rgba(0,0,0,.18)}
  .panel{position:relative;height:100%;overflow:hidden}

  /* Inside panel */
  .panel--benefits{width:371px;background:var(--white)}
  .photo{position:absolute}
  .benefits__photo{left:0;top:0;width:371px;height:300px;background:linear-gradient(120deg,#dfe6ee,#c9d3de 45%,#b9c6d3 70%,#e8ecf0)}
  .benefits__curve{position:absolute;left:0;top:270px;width:371px;height:50px}
  .badge{position:absolute;left:231px;top:256px;width:96px;height:96px;border-radius:50%;background:var(--navy);border:5px solid var(--white);box-shadow:0 0 0 2px var(--blue)}
  .benefits__title{position:absolute;left:40px;top:312px;font-size:15px;font-weight:700;line-height:19px;color:var(--navy)}
  .benefits__title span{color:var(--olive)}
  .benefits__list{position:absolute;left:40px;top:363px;list-style:none;font-size:12.5px;color:var(--ink)}
  .benefits__list li{position:relative;padding-left:15px;line-height:16px;margin-bottom:6px}
  .benefits__list li::before{content:"";position:absolute;left:0;top:4px;width:9px;height:9px;border-radius:50%;background:var(--blue)}
  .pricing{position:absolute;left:42px;top:521px;width:288px;height:165px;border:2px solid var(--navy);border-radius:4px}
  .pricing__tab{position:absolute;left:-2px;top:-10px;background:var(--navy);color:var(--white);font-size:12px;font-weight:500;padding:3px 10px 3px 8px;border-radius:0 10px 0 0}
  .pricing__rows{position:absolute;left:8px;right:10px;top:16px;font-size:12.3px;color:var(--ink)}
  .pricing__row{display:flex;justify-content:space-between;line-height:15px;margin-bottom:7px}
  .pricing__row small{display:block;font-size:12.3px}
  .benefits__footer{position:absolute;left:0;top:701px;width:371px;height:162px;background:var(--sky)}
  .footer__name{position:absolute;left:0;width:100%;top:36px;text-align:center;font-size:26px;font-weight:500;color:var(--blue);letter-spacing:.5px}
  .footer__contact{position:absolute;top:92px;font-size:11px;line-height:14.5px;color:var(--ink)}
  .footer__contact--addr{left:38px}
  .footer__contact--links{left:218px}
  .footer__contact svg{width:10px;height:10px;vertical-align:-1px;margin-right:4px}

  /* Contact panel */
  .panel--contact{width:368px;background:linear-gradient(180deg,#0b8a3e 0%,#0c6a4a 28%,#0d2e62 58%,var(--navy) 80%,var(--navy-deep) 100%)}
  .contact__photo{left:0;top:0;width:368px;height:190px;background:linear-gradient(180deg,rgba(20,120,60,.9),rgba(10,110,70,0));opacity:.8}
  .contact__name{position:absolute;left:0;width:100%;top:388px;text-align:center;font-size:33px;font-weight:500;color:var(--white);letter-spacing:.5px}
  .contact__title{position:absolute;left:0;width:100%;top:533px;text-align:center;font-size:24px;font-weight:900;color:var(--green-bright)}
  .contact__item{position:absolute;left:0;width:100%;text-align:center;color:var(--white);font-size:14.5px;line-height:20px}
  .icon{display:block;margin:0 auto 6px;width:22px;height:22px}

  /* Cover panel */
  .panel--cover{width:381px;background:var(--white)}
  .cover__name{position:absolute;left:0;width:100%;top:56px;text-align:center;font-size:34px;font-weight:500;color:var(--blue);letter-spacing:.5px}
  .cover__photo{left:0;top:136px;width:381px;height:450px;background:linear-gradient(110deg,#f1f3f5 0%,#dfe3e6 30%,#c6cdd4 55%,#eef0f2 80%,#d9dde1)}
  .cover__band{position:absolute;left:0;top:540px;width:381px;height:323px}
  .cover__tagline{position:absolute;left:0;width:100%;top:610px;text-align:center;color:var(--white);font-size:24px;line-height:34px}
  .cover__rule{position:absolute;left:30px;width:321px;top:697px;height:1px;background:rgba(255,255,255,.25)}
  .cover__headline{position:absolute;left:0;width:100%;top:714px;text-align:center;color:var(--white);font-size:29px;font-weight:700;line-height:40px}
  .cover__url{position:absolute;left:0;width:100%;top:817px;height:25px;background:var(--white);text-align:center;font-size:14px;letter-spacing:5px;line-height:25px;color:var(--ink)}
</style>
</head>
<body>
<main class="trifold">

  <section class="panel panel--benefits">
    <div class="photo benefits__photo" role="img" aria-label="Photo of a doctor with a tablet talking with an older patient"></div>
    <svg class="benefits__curve" viewBox="0 0 371 50" preserveAspectRatio="none">
      <path d="M0 30 Q185 0 371 24 L371 50 L0 50Z" fill="#fff"/>
      <path d="M0 30 Q185 0 371 24" fill="none" stroke="#0a8a3c" stroke-width="3"/>
    </svg>
    <div class="badge" aria-hidden="true"></div>
    <h2 class="benefits__title">WHY CHOOSE DIRECT<br><span>PRIMARY CARE?</span></h2>
    <ul class="benefits__list">
      <li>24/7 access to your doctor via telemedicine,<br>text, and phone consultations</li>
      <li>Same day or next day appointments</li>
      <li>Low cost labs</li>
      <li>Wellness planning and health screenings</li>
      <li>Unlimited appointments</li>
    </ul>
    <div class="pricing">
      <div class="pricing__tab">Direct Primary Care Pricing</div>
      <div class="pricing__rows">
        <div class="pricing__row"><span>Enrollment (Individual):</span><span>$60</span></div>
        <div class="pricing__row"><span>Enrollment (Family):</span><span>$120</span></div>
        <div class="pricing__row"><span>Monthly Membership:<small>(child added to adult membership)</small></span><span>$10</span></div>
        <div class="pricing__row"><span>Monthly Membership (age 19- 49):</span><span>$60</span></div>
        <div class="pricing__row"><span>Monthly Membership (age 50-64):</span><span>$75</span></div>
        <div class="pricing__row"><span>Monthly Membership (age 65-up):</span><span>$95</span></div>
      </div>
    </div>
    <footer class="benefits__footer">
      <div class="footer__name">Velbrook Health</div>
      <div class="footer__contact footer__contact--addr">
        <svg viewBox="0 0 10 10"><path d="M5 0a3.4 3.4 0 0 0-3.4 3.4C1.6 6 5 10 5 10s3.4-4 3.4-6.6A3.4 3.4 0 0 0 5 0Zm0 4.8a1.4 1.4 0 1 1 0-2.8 1.4 1.4 0 0 1 0 2.8Z" fill="#333"/></svg>1820 Alder Ridge Road<br>&nbsp;&nbsp;&nbsp;&nbsp;Suite C Marlow,<br>&nbsp;&nbsp;&nbsp;&nbsp;GA 30190
      </div>
      <div class="footer__contact footer__contact--links">
        <svg viewBox="0 0 10 10"><path d="M2 0.5 3.6 2.6 2.7 3.8Q4 6.3 6.2 7.3L7.4 6.4 9.5 8 8.4 9.5Q3 8.5 0.5 1.6Z" fill="#333"/></svg>555-014-2290<br>
        <svg viewBox="0 0 10 10"><rect x="0.5" y="2" width="9" height="6" fill="#333"/></svg>info@velbrook.example<br>
        <svg viewBox="0 0 10 10"><circle cx="5" cy="5" r="4" fill="#333"/></svg>www.velbrook.example
      </div>
    </footer>
  </section>

  <section class="panel panel--contact">
    <div class="photo contact__photo" role="img" aria-label="Faint green-toned photo of a caregiver holding an older person's hand"></div>
    <div class="contact__name">Velbrook Health</div>
    <h2 class="contact__title">CONTACT INFO</h2>
    <div class="contact__item" style="top:584px">
      <svg class="icon" viewBox="0 0 22 22"><circle cx="11" cy="11" r="10" fill="none" stroke="#fff" stroke-width="1.4"/><path d="M11 5a3.5 3.5 0 0 0-3.5 3.5C7.5 11.5 11 16 11 16s3.5-4.5 3.5-7.5A3.5 3.5 0 0 0 11 5Zm0 5a1.4 1.4 0 1 1 0-2.8 1.4 1.4 0 0 1 0 2.8Z" fill="#fff"/></svg>
      1820 Alder Ridge Road<br>Suite C Marlow, GA 30190
    </div>
    <div class="contact__item" style="top:664px">
      <svg class="icon" viewBox="0 0 22 22"><circle cx="11" cy="11" r="10" fill="none" stroke="#fff" stroke-width="1.4"/><path d="M7.5 5.5 9.3 8 8.3 9.3Q9.6 12 12.6 13.6L13.8 12.6 16.3 14.4 15 16.2Q8 15 5.8 7Z" fill="#fff"/></svg>
      555-014-2290
    </div>
    <div class="contact__item" style="top:724px">
      <svg class="icon" viewBox="0 0 22 22"><circle cx="11" cy="11" r="10" fill="none" stroke="#fff" stroke-width="1.4"/><rect x="6" y="7.5" width="10" height="7" fill="none" stroke="#fff" stroke-width="1.3"/><path d="M6 7.5 11 11.5 16 7.5" fill="none" stroke="#fff" stroke-width="1.3"/></svg>
      info@velbrook.example
    </div>
    <div class="contact__item" style="top:784px">
      <svg class="icon" viewBox="0 0 22 22"><circle cx="11" cy="11" r="10" fill="none" stroke="#fff" stroke-width="1.4"/><circle cx="11" cy="11" r="5.5" fill="none" stroke="#fff" stroke-width="1.2"/><path d="M5.5 11h11M11 5.5c-2.5 3-2.5 8 0 11M11 5.5c2.5 3 2.5 8 0 11" fill="none" stroke="#fff" stroke-width="1.1"/></svg>
      www.velbrook.example
    </div>
  </section>

  <section class="panel panel--cover">
    <div class="cover__name">Velbrook Health</div>
    <div class="photo cover__photo" role="img" aria-label="Photo of a doctor listening to a young woman's heartbeat with a stethoscope"></div>
    <svg class="cover__band" viewBox="0 0 381 323" preserveAspectRatio="none">
      <defs>
        <linearGradient id="coverNavy" x1="0" y1="0" x2="0" y2="1">
          <stop offset="0" stop-color="#0d2c62"/>
          <stop offset=".35" stop-color="#0d1656"/>
          <stop offset="1" stop-color="#0a1248"/>
        </linearGradient>
      </defs>
      <path d="M0 56 Q150 0 381 60 L381 323 L0 323Z" fill="#0a8a3c"/>
      <path d="M0 66 Q150 14 381 72 L381 323 L0 323Z" fill="url(#coverNavy)"/>
    </svg>
    <p class="cover__tagline">It is Possible to<br>Pay less and Get more</p>
    <div class="cover__rule"></div>
    <h1 class="cover__headline">Velbrook Health<br>Direct primary Care</h1>
    <div class="cover__url">www.velbrook.example</div>
  </section>

</main>
</body>
</html>
```